New Web Design Project

See attachments on the content and concept. Very important that the flow of the tiers stand out

Target Market(s)

Food and Beverage Manufacturing

Industry/Entity Type

Food and Beverage

Coding

Coded - Design and coding required

Number of Pages Required

3 page

Colors
0054AA
0677BA
7BADD7
CADEEF
E8F1F8

```html
<!DOCTYPE html>
<html lang="en">
<head>
<meta charset="utf-8">
<title>Northfield Compliance Group — SQF Consulting</title>
<link rel="stylesheet" href="https://fonts.googleapis.com/css2?family=Libre+Baskerville:wght@400;700&family=Poppins:wght@400;500;600;700&display=swap">
<style>
:root{
  --blue:#0054AA;
  --blue-mid:#0677BA;
  --blue-soft:#7BADD7;
  --blue-pale:#CADEEF;
  --blue-wash:#E8F1F8;
  --navy:#0f1d31;
  --ink:#16202c;
  --muted:#4a5563;
  --line:#dfe3e8;
  --white:#ffffff;
  --serif:'Libre Baskerville', Georgia, serif;
  --sans:'Poppins', Arial, sans-serif;
}
*{box-sizing:border-box;margin:0;padding:0}
html,body{width:1200px;height:4301px;overflow:hidden}
body{position:relative;background:var(--white);font-family:var(--sans);color:var(--ink)}
.abs{position:absolute}
h1,h2,h3,.serif{font-family:var(--serif);font-weight:700;text-transform:uppercase;letter-spacing:0}
.tag{display:inline-block;background:#e3e5e8;color:#333;font-size:9px;padding:4px 12px;border-radius:3px;text-transform:uppercase;letter-spacing:.03em}
.btn{display:inline-flex;align-items:center;justify-content:center;font-size:9.5px;font-weight:700;text-transform:uppercase;letter-spacing:.04em;border-radius:4px;text-decoration:none;white-space:nowrap}
.btn-solid{background:var(--blue);color:var(--white)}
.btn-ghost{border:1.5px solid var(--white);color:var(--white)}
.btn-line{border:1.5px solid var(--ink);color:var(--ink);background:var(--white)}

/* brand */
.brand{display:flex;align-items:center;gap:8px}
.brand-dot{width:34px;height:34px;border-radius:50%;border:2px solid currentColor;flex:none}
.brand-name{font-family:var(--serif);font-weight:700;font-size:17px;line-height:1;white-space:nowrap;letter-spacing:-.01em}
.brand-sub{font-size:8px;letter-spacing:.12em;text-transform:uppercase;margin-top:4px;white-space:nowrap}

/* hero */
.hero{position:absolute;left:0;top:0;width:1200px;height:689px;background:linear-gradient(100deg,#1e2a3a 0%,#3b4858 40%,#8c98a6 70%,#c5ccd4 100%)}
.hero-shade{position:absolute;inset:0;background:linear-gradient(90deg,rgba(15,25,40,.75) 0%,rgba(15,25,40,.35) 55%,rgba(15,25,40,.05) 100%)}
.nav{position:absolute;left:133px;top:20px;width:935px;height:40px;display:flex;align-items:center;justify-content:space-between;color:var(--white)}
.nav-links{display:flex;gap:40px;align-items:center;font-size:10px;letter-spacing:.04em;margin-left:auto;margin-right:32px}
.nav .btn{width:170px;height:38px}
.hero-copy{position:absolute;left:133px;top:216px;width:470px;color:var(--white)}
.hero-copy .tag{background:rgba(255,255,255,.18);color:var(--white)}
.hero-copy h1{font-size:29px;line-height:37px;margin:16px 0 18px;letter-spacing:-.005em}
.hero-copy p{font-size:10px;line-height:15px;width:400px}
.hero-actions{display:flex;gap:8px;margin-top:20px}
.hero-actions .btn{height:38px}

/* stats */
.stats{position:absolute;left:0;top:689px;width:1200px;height:137px;background:var(--blue);color:var(--white)}
.stat{position:absolute;top:38px}
.stat b{display:block;font-family:var(--serif);font-size:32px;line-height:34px}
.stat span{display:block;font-family:var(--serif);font-weight:700;font-size:13px;margin-top:4px;white-space:nowrap}
.stat-rule{position:absolute;top:20px;width:1px;height:97px;background:rgba(255,255,255,.25)}

/* services */
.section-head{position:absolute;left:0;width:1200px;text-align:center}
.section-head h2{font-size:27px;line-height:35px;margin-top:14px}
.section-head p{font-size:10px;line-height:15px;color:var(--muted);margin:14px auto 0;width:560px}
.svc{position:absolute;width:295px;height:234px;border:1px solid var(--line);border-radius:14px;padding:44px 20px 0;background:var(--white)}
.svc.featured{background:var(--blue);border-color:var(--blue);color:var(--white)}
.svc svg{width:50px;height:50px;display:block;margin-bottom:22px}
.svc h3{font-size:13px;margin-bottom:10px;white-space:nowrap}
.svc p{font-size:9.5px;line-height:15px;color:var(--muted)}
.svc.featured p{color:var(--white)}

/* why */
.why{position:absolute;left:0;top:1677px;width:1200px;height:723px;background:var(--blue-wash)}
.benefit{position:absolute;width:330px}
.benefit h3{font-size:12.5px;margin-bottom:8px;white-space:nowrap}
.benefit p{font-size:9.5px;line-height:15px;color:var(--muted)}
.benefit.left{text-align:right}
.tick{position:absolute;width:24px;height:24px}

/* process */
.step{position:absolute;width:425px;height:107px;background:var(--white);border-radius:10px;box-shadow:0 4px 18px rgba(20,40,70,.10);padding:18px 20px 0 96px}
.step svg{position:absolute;left:14px;top:16px;width:72px;height:76px}
.step h3{font-size:12.5px;margin-bottom:7px}
.step p{font-size:9.5px;line-height:15px;color:var(--muted)}

/* quote */
.quote{position:absolute;left:0;top:2951px;width:1200px;height:554px;background:var(--blue-wash)}
.quote-art{position:absolute;left:147px;top:95px;width:283px;height:335px;border-radius:40px 40px 140px 140px;background:linear-gradient(160deg,#d7e3ee 0%,#b9c9da 100%)}
.quote-body{position:absolute;left:489px;top:143px;width:580px}
.quote blockquote{font-family:var(--serif);font-weight:700;text-transform:uppercase;font-size:26px;line-height:34.5px;color:var(--navy)}
.quote cite{display:block;margin-top:22px;font-style:normal;font-size:9px;font-weight:700;color:var(--blue);letter-spacing:.04em}

/* creds */
.creds{position:absolute;left:0;top:3505px;width:1200px;height:222px;background:var(--blue);color:var(--white)}
.cred{position:absolute;top:62px;width:230px;text-align:center}
.cred svg{width:52px;height:52px;display:block;margin:0 auto 12px}
.cred span{font-family:var(--serif);font-weight:700;font-size:13px;white-space:nowrap}
.cred-rule{position:absolute;top:45px;width:1px;height:130px;background:rgba(255,255,255,.25)}

/* cta */
.cta h2{position:absolute;left:230px;top:3803px;font-size:28px}
.cta p{position:absolute;left:230px;top:3854px;width:440px;font-size:9.5px;line-height:15px;color:var(--muted)}
.cta .btn{position:absolute;left:733px;width:235px;height:37px}

/* footer */
.rule{position:absolute;left:130px;width:940px;height:1px;background:#c9ced4}
.foot-col{position:absolute;top:4031px}
.foot-col h4{font-family:var(--serif);font-weight:700;font-size:15px;text-transform:uppercase;margin-bottom:12px}
.foot-col li{list-style:none;font-size:9.5px;line-height:19px;color:var(--muted);display:flex;align-items:center;gap:6px}
.foot-col li svg{width:9px;height:9px}
.contact-item{font-size:9.5px;line-height:14px;color:var(--muted);margin-bottom:10px;padding-left:16px;position:relative}
.contact-item b{display:block;color:var(--ink);font-weight:600;text-transform:uppercase;font-size:10px}
.contact-item svg{position:absolute;left:0;top:2px;width:9px;height:9px}
.socials{display:flex;gap:6px}
.socials i{width:18px;height:18px;border-radius:50%;background:var(--blue);display:block}
.copyright{position:absolute;left:0;top:4265px;width:1200px;text-align:center;font-size:9px;color:var(--muted)}
.chat{position:absolute;left:1122px;top:4233px;width:34px;height:34px;border-radius:50%;background:var(--blue)}
</style>
</head>
<body>

<!-- HERO -->
<section class="hero">
  <div class="hero-shade" role="img" aria-label="Photo of a lab technician in protective clothing using a microscope in a clean food production facility"></div>
  <header class="nav">
    <div class="brand">
      <span class="brand-dot"></span>
      <div>
        <div class="brand-name">Northfield Compliance Group</div>
        <div class="brand-sub">Food Safety &amp; SQF Certification</div>
      </div>
    </div>
    <nav class="nav-links">
      <span>SERVICES</span><span>BENEFITS</span><span>PROCESS</span><span>CONTACT</span>
      <svg width="16" height="16" viewBox="0 0 16 16" fill="none" stroke="#fff" stroke-width="1.4"><path d="M12 10.5A5.5 5.5 0 0 1 5.5 4a5.5 5.5 0 1 0 6.5 6.5z"/></svg>
    </nav>
    <a class="btn btn-solid">Get SQF Consultation</a>
  </header>
  <div class="hero-copy">
    <span class="tag">SQF Only · Tech Driven</span>
    <h1>Hire a tech-driven SQF<br>team that carries<br>you across the<br>certification finish</h1>
    <p>At Northfield Compliance Group, we focus exclusively on SQF — combining real plant experience with smart technology so your team can stay focused on production while we handle the path to certification and beyond.</p>
    <div class="hero-actions">
      <a class="btn btn-solid" style="width:169px">Get SQF Consultation</a>
      <a class="btn btn-ghost" style="width:127px">Explore Services</a>
    </div>
  </div>
</section>

<!-- STATS -->
<section class="stats">
  <div class="stat" style="left:133px"><b>15+</b><span>CLIENTS ONBOARDED</span></div>
  <div class="stat-rule" style="left:327px"></div>
  <div class="stat" style="left:359px"><b>100%</b><span>SQF FOCUSED</span></div>
  <div class="stat-rule" style="left:554px"></div>
  <div class="stat" style="left:586px"><b>DIGITAL</b><span>PLATFORM BUILT PROGRAMS</span></div>
  <div class="stat-rule" style="left:848px"></div>
  <div class="stat" style="left:880px"><b>US</b><span>NATIONWIDE COVERAGE</span></div>
</section>

<!-- SERVICES -->
<div class="section-head" style="top:914px">
  <span class="tag">What We Do</span>
  <h2>SQF Consulting, Implementation<br>&amp; Onboarding</h2>
  <p>We help food and beverage manufacturers achieve and maintain SQF certification with confidence, using practical programs and digital tools that work on the floor — not just on audit day.</p>
</div>

<article class="svc" style="left:145px;top:1097px">
  <svg viewBox="0 0 50 50" fill="none" stroke="#16202c" stroke-width="1.6"><circle cx="25" cy="25" r="14"/><circle cx="25" cy="25" r="20" stroke-dasharray="5 4"/><path d="M21 21l-4 4 4 4M29 21l4 4-4 4"/></svg>
  <h3>SQF Program Design</h3>
  <p>We design your complete SQF system from scratch — HACCP/food safety plans, prerequisite programs, SOPs, forms, logs, and all required documentation tailored to your facility.</p>
</article>
<article class="svc featured" style="left:452px;top:1097px">
  <svg viewBox="0 0 50 50" fill="none" stroke="#fff" stroke-width="1.6"><circle cx="20" cy="16" r="6"/><circle cx="34" cy="12" r="4"/><rect x="12" y="30" width="26" height="10" rx="2"/><path d="M8 44h34M25 22v8"/></svg>
  <h3>Digital Platform Build</h3>
  <p>We build your SQF program directly into modern food safety software like SafeBatch.io or PlantLedger.io — digitizing forms, checklists, monitoring logs, and workflows so your team runs paperless.</p>
</article>
<article class="svc" style="left:761px;top:1097px">
  <svg viewBox="0 0 50 50" fill="none" stroke="#16202c" stroke-width="1.6"><rect x="14" y="8" width="22" height="20" rx="2"/><path d="M18 14h14M18 19h14M18 24h8"/><circle cx="12" cy="32" r="4"/><circle cx="38" cy="32" r="4"/><path d="M6 44v-4a6 6 0 0 1 12 0v4M32 44v-4a6 6 0 0 1 12 0v4"/></svg>
  <h3>Coaching &amp; Support</h3>
  <p>After building your system, we coach your team to own and maintain it day-to-day. You run the program; we provide ongoing expert guidance so you stay audit-ready at all times.</p>
</article>
<article class="svc" style="left:145px;top:1344px">
  <svg viewBox="0 0 50 50" fill="none" stroke="#16202c" stroke-width="1.6"><rect x="8" y="6" width="24" height="32" rx="2"/><path d="M13 13h14M13 19h14M13 25h8"/><circle cx="34" cy="34" r="7"/><path d="M39 39l6 6"/></svg>
  <h3>Gap Assessments</h3>
  <p>We evaluate where your facility stands against SQF requirements, identify gaps, and provide a clear roadmap to close them before your audit — no surprises on certification day.</p>
</article>
<article class="svc" style="left:452px;top:1344px">
  <svg viewBox="0 0 50 50" fill="none" stroke="#16202c" stroke-width="1.6"><circle cx="18" cy="18" r="7"/><path d="M6 42v-6a12 12 0 0 1 24 0v6"/><rect x="30" y="8" width="14" height="10" rx="2"/><path d="M30 30h14v10H30z"/></svg>
  <h3>Bilingual Team Support</h3>
  <p>Our team in Central America supports Spanish-speaking employees within your operation — delivering training, documentation, and coaching in the language your floor team actually speaks.</p>
</article>
<article class="svc" style="left:761px;top:1344px">
  <svg viewBox="0 0 50 50" fill="none" stroke="#16202c" stroke-width="1.6"><circle cx="25" cy="25" r="19"/><path d="M12 12l26 26"/><path d="M19 30l6-12 6 8"/></svg>
  <h3>Sanitation &amp; Regulatory</h3>
  <p>From sanitation program design to environmental monitoring, we help you build internal capabilities that meet USDA, FDA, and FSMA requirements and reduce dependence on external contractors.</p>
</article>

<!-- WHY -->
<section class="why">
  <div class="section-head" style="top:56px">
    <span class="tag">Why Northfield</span>
    <h2 style="margin-top:12px">Built for Small &amp; Mid Size Manufacturers</h2>
    <p style="margin-top:8px;width:760px">You don't need to hire a full-time food safety director or figure out SQF alone. We bring the expertise and technology you stay focused on production.</p>
  </div>

  <svg class="abs" style="left:459px;top:184px" width="284" height="330" viewBox="0 0 284 330">
    <defs>
      <clipPath id="shield-inner"><path d="M142 24 L258 70 V170 C258 250 200 296 142 306 C84 296 26 250 26 170 V70 Z"/></clipPath>
      <linearGradient id="photo-tone" x1="0" y1="0" x2="1" y2="1"><stop offset="0" stop-color="#dfe6ee"/><stop offset=".6" stop-color="#9fb3c9"/><stop offset="1" stop-color="#5c7797"/></linearGradient>
    </defs>
    <path d="M142 2 L282 56 V170 C282 266 212 320 142 330 C72 320 2 266 2 170 V56 Z" fill="#0f1d31"/>
    <path d="M142 18 L264 66 V170 C264 256 202 302 142 312 C82 302 20 256 20 170 V66 Z" fill="#ffffff"/>
    <g clip-path="url(#shield-inner)"><rect x="0" y="0" width="284" height="330" fill="url(#photo-tone)" role="img" aria-label="Photo of a quality manager reviewing food safety data on a tablet in a production plant"/></g>
  </svg>

  <svg class="tick" style="left:424px;top:252px" viewBox="0 0 24 24" fill="none" stroke="#16202c" stroke-width="1.6"><circle cx="12" cy="12" r="11"/><path d="M7 12l3.5 3.5L17 9"/></svg>
  <div class="benefit left" style="left:86px;top:254px">
    <h3>Lower Cost Than a Full-Time Hire</h3>
    <p>Get a complete SQF team — program design, digital implementation, and coaching — at a fraction of the cost of hiring a full-time SQF Practitioner.</p>
  </div>
  <svg class="tick" style="left:424px;top:398px" viewBox="0 0 24 24" fill="none" stroke="#16202c" stroke-width="1.6"><circle cx="12" cy="12" r="11"/><path d="M7 12l3.5 3.5L17 9"/></svg>
  <div class="benefit left" style="left:86px;top:400px">
    <h3>Your Program Lives in Software</h3>
    <p>No more binders and spreadsheets. Your SQF system is built into SafeBatch.io or PlantLedger.io — organized, accessible, and always audit-ready.</p>
  </div>

  <svg class="tick" style="left:755px;top:252px" viewBox="0 0 24 24" fill="none" stroke="#16202c" stroke-width="1.6"><circle cx="12" cy="12" r="11"/><path d="M7 12l3.5 3.5L17 9"/></svg>
  <div class="benefit" style="left:793px;top:254px">
    <h3>You Own It, We Support It</h3>
    <p>We build the system and train your team. You maintain and run it day-to-day. We stay on call with coaching and advisory so you never feel stuck.</p>
  </div>
  <svg class="tick" style="left:755px;top:398px" viewBox="0 0 24 24" fill="none" stroke="#16202c" stroke-width="1.6"><circle cx="12" cy="12" r="11"/><path d="M7 12l3.5 3.5L17 9"/></svg>
  <div class="benefit" style="left:793px;top:400px">
    <h3>Flexible, Low-Risk Engagement</h3>
    <p>Start with a 3-month commitment, then go month-to-month. Cancel anytime with 30 days notice. We earn your business every month.</p>
  </div>

  <svg class="tick" style="left:588px;top:542px" viewBox="0 0 24 24" fill="none" stroke="#16202c" stroke-width="1.6"><circle cx="12" cy="12" r="11"/><path d="M7 12l3.5 3.5L17 9"/></svg>
  <div class="benefit" style="left:380px;top:576px;width:440px;text-align:center">
    <h3>Bilingual Floor-Level Support</h3>
    <p>With our Central America team, we provide training and documentation in Spanish so every member of your production team understands and follows the program.</p>
  </div>
</section>

<!-- PROCESS -->
<div class="abs" style="left:167px;top:2508px">
  <span class="tag">How It Works</span>
  <h2 style="font-size:28px;margin-top:12px">From Discovery to Certification</h2>
  <p style="font-size:9.5px;color:var(--muted);margin-top:10px">A clear, structured path that takes the guesswork out of SQF.</p>
</div>

<article class="step" style="left:167px;top:2630px">
  <svg viewBox="0 0 72 76" fill="none" stroke="#0f1d31"><path d="M36 2L70 14V38C70 58 52 72 36 74C20 72 2 58 2 38V14Z" stroke-width="3"/><circle cx="36" cy="38" r="18" stroke-width="1.5"/><path d="M29 32c2-3 5-3 7 0l-2 3 4 4 3-2c3 2 3 5 0 7-6 2-14-6-12-12z" stroke-width="1.5"/></svg>
  <h3>Discovery Call</h3>
  <p>We learn about your facility, your current systems, and where you are in the SQF journey. No pressure — just a conversation.</p>
</article>
<article class="step" style="left:606px;top:2630px">
  <svg viewBox="0 0 72 76" fill="none" stroke="#0f1d31"><path d="M36 2L70 14V38C70 58 52 72 36 74C20 72 2 58 2 38V14Z" stroke-width="3"/><circle cx="36" cy="38" r="18" stroke-width="1.5"/><rect x="29" y="30" width="14" height="16" rx="1.5" stroke-width="1.5"/><path d="M32 35h8M32 40h8" stroke-width="1.5"/></svg>
  <h3>Build &amp; Implement</h3>
  <p>We design your SQF program and build it directly into your digital food safety platform — forms, logs, SOPs, HACCP plans, all of it.</p>
</article>
<article class="step" style="left:167px;top:2750px">
  <svg viewBox="0 0 72 76" fill="none" stroke="#0f1d31"><path d="M36 2L70 14V38C70 58 52 72 36 74C20 72 2 58 2 38V14Z" stroke-width="3"/><circle cx="36" cy="38" r="18" stroke-width="1.5"/><circle cx="34" cy="36" r="6" stroke-width="1.5"/><path d="M38.5 40.5l5 5" stroke-width="1.5"/></svg>
  <h3>Gap Assessment</h3>
  <p>We evaluate your facility against SQF requirements, identify what's missing, and give you a clear roadmap with priorities.</p>
</article>
<article class="step" style="left:606px;top:2750px">
  <svg viewBox="0 0 72 76" fill="none" stroke="#0f1d31"><path d="M36 2L70 14V38C70 58 52 72 36 74C20 72 2 58 2 38V14Z" stroke-width="3"/><circle cx="36" cy="38" r="18" stroke-width="1.5"/><path d="M29 38l5 5 9-10" stroke-width="1.8"/></svg>
  <h3>Coach &amp; Certify</h3>
  <p>We train your team, run mock audits, and prepare you for certification day. Then we stay on as your ongoing SQF advisory partner.</p>
</article>

<!-- TESTIMONIAL -->
<section class="quote">
  <div class="quote-art" role="img" aria-label="Illustration of a shield with a checkmark symbolising certification"></div>
  <div class="quote-body">
    <blockquote>Northfield Compliance Group didn't just hand us a binder. They built our entire SQF system into software and coached our team until we owned it. We passed our first audit with confidence.</blockquote>
    <cite>— SQF-CERTIFIED MANUFACTURING CLIENT</cite>
  </div>
</section>

<!-- CREDENTIALS -->
<section class="creds">
  <div class="cred" style="left:136px">
    <svg viewBox="0 0 52 52" fill="none" stroke="#fff" stroke-width="1.6"><circle cx="26" cy="16" r="8"/><path d="M10 48v-8a16 16 0 0 1 32 0v8"/><rect x="34" y="4" width="12" height="14" rx="2"/></svg>
    <span>SQF PRACTITIONER</span>
  </div>
  <div class="cred-rule" style="left:367px"></div>
  <div class="cred" style="left:382px">
    <svg viewBox="0 0 52 52" fill="none" stroke="#fff" stroke-width="1.6"><ellipse cx="26" cy="20" rx="20" ry="10"/><path d="M16 28l-6 18M36 28l6 18M20 22l12-4"/></svg>
    <span>SIX SIGMA BLACK BELT</span>
  </div>
  <div class="cred-rule" style="left:631px"></div>
  <div class="cred" style="left:634px">
    <svg viewBox="0 0 52 52" fill="none" stroke="#fff" stroke-width="1.6"><rect x="16" y="8" width="20" height="36" rx="4" transform="rotate(35 26 26)"/><path d="M40 6a8 8 0 0 1 6 6M38 2a14 14 0 0 1 12 12"/></svg>
    <span>REMOTE &amp; ON-SITE</span>
  </div>
  <div class="cred-rule" style="left:863px"></div>
  <div class="cred" style="left:851px">
    <svg viewBox="0 0 52 52" fill="none" stroke="#fff" stroke-width="1.6"><circle cx="26" cy="24" r="10"/><path d="M26 4v10M10 10l7 7M42 10l-7 7M4 24h10M38 24h10M22 34v10h8V34"/></svg>
    <span>DIGITAL-FIRST</span>
  </div>
</section>

<!-- CTA -->
<section class="cta">
  <h2>Ready to Talk SQF?</h2>
  <p>Share a few details about your facility and where you are in the SQF journey. We'll follow up with a brief discovery call and a clear next step.</p>
  <a class="btn btn-solid" style="top:3810px">Get My SQF Consultation</a>
  <a class="btn btn-line" style="top:3855px">Visit northfieldcompliance.co</a>
</section>

<div class="rule" style="top:3961px"></div>

<!-- FOOTER -->
<footer>
  <div class="foot-col" style="left:161px;top:4040px;width:290px">
    <div class="brand" style="color:var(--ink)">
      <span class="brand-dot"></span>
      <div>
        <div class="brand-name" style="font-size:16px">Northfield Compliance Group</div>
        <div class="brand-sub" style="color:var(--muted)">Food Safety &amp; SQF Certification</div>
      </div>
    </div>
    <p style="font-size:9.5px;line-height:15px;color:var(--muted);margin-top:16px;width:280px">Tech-driven SQF consulting for small and mid-size US food manufacturers. Based in Riverton, CA — serving clients across North America.</p>
  </div>
  <div class="foot-col" style="left:515px">
    <h4>Services</h4>
    <ul>
      <li><svg viewBox="0 0 10 10" fill="none" stroke="#0f1d31" stroke-width="1.6"><path d="M1 5l3 3 5-6"/></svg>SQF Program Design</li>
      <li><svg viewBox="0 0 10 10" fill="none" stroke="#0f1d31" stroke-width="1.6"><path d="M1 5l3 3 5-6"/></svg>Digital Platform Build</li>
      <li><svg viewBox="0 0 10 10" fill="none" stroke="#0f1d31" stroke-width="1.6"><path d="M1 5l3 3 5-6"/></svg>Coaching &amp; Support</li>
      <li><svg viewBox="0 0 10 10" fill="none" stroke="#0f1d31" stroke-width="1.6"><path d="M1 5l3 3 5-6"/></svg>Gap Assessments</li>
      <li><svg viewBox="0 0 10 10" fill="none" stroke="#0f1d31" stroke-width="1.6"><path d="M1 5l3 3 5-6"/></svg>Sanitation Programs</li>
    </ul>
  </div>
  <div class="foot-col" style="left:709px;width:180px">
    <h4>Connect</h4>
    <div class="contact-item"><svg viewBox="0 0 10 10" fill="#5b4a8a"><rect x="0" y="2" width="10" height="7" rx="1"/></svg><b>Email Us</b>hello@northfieldcompliance.co</div>
    <div class="contact-item"><svg viewBox="0 0 10 10" fill="#5b4a8a"><path d="M2 0l2 2-1 2a6 6 0 0 0 3 3l2-1 2 2-1 2C4 10 0 6 0 1z"/></svg><b>Phone</b>(555) 014-2290</div>
    <div class="contact-item"><svg viewBox="0 0 10 10" fill="#5b4a8a"><path d="M5 0a3.5 3.5 0 0 1 3.5 3.5C8.5 6 5 10 5 10S1.5 6 1.5 3.5A3.5 3.5 0 0 1 5 0z"/></svg><b>Email Address</b>Reference site about Lorem Ipsum, giving information on its origins.</div>
  </div>
  <div class="foot-col" style="left:925px">
    <h4>Follow Me</h4>
    <div class="socials"><i></i><i></i><i></i><i></i><i></i></div>
  </div>
</footer>

<div class="rule" style="top:4243px"></div>
<p class="copyright">© 2026 Northfield Compliance Group LLC. All rights reserved. Created with Northfield Studio</p>
<div class="chat" aria-label="Chat"><svg width="34" height="34" viewBox="0 0 34 34" fill="none" stroke="#fff" stroke-width="1.6"><path d="M9 11h16v10H15l-4 3v-3H9z"/></svg></div>

</body>
</html>
```